Business card design needed

A laid back coffee shop that has a great feel, that becomes a bar and grill at night. We are also wanting to cater for functions etc.
The business itself is painted dark blue/charcoal and has red doors.
Would like a logo that will be recognised when seen.

Industry/Entity Type

Coffee Shop

Contact Information for Business Card

The Lantern Coffee Bar & Grill
14b Wattlebrook St
Kelmarra NSW 2318
Ph. 02 4817 6293

Logo Text

Logo styles of interest
Emblem Logo
Abstract Logo
Wordmark Logo
Requirements
Must have
• A loyalty card on the back with 2 rows of 7 stamp spaces and a place to write a name and phone number (for a draw)

```html
<!DOCTYPE html>
<html lang="en">
<head>
<meta charset="utf-8">
<title>The Lantern Coffee Bar &amp; Grill – Business Card</title>
<link rel="stylesheet" href="https://fonts.googleapis.com/css2?family=Nunito+Sans:wght@400&family=Courier+Prime&display=swap">
<style>
  :root {
    --page: #ffffff;
    --card: #2b2b2b;
    --ink-light: #ffffff;
    --slot: #ffffff;
    --stamp: #ef4b52;
    --label: #c4c4c4;
  }
  html, body {
    margin: 0;
    padding: 0;
    width: 1200px;
    height: 859px;
    overflow: hidden;
    background: var(--page);
  }
  .canvas {
    position: relative;
    width: 1200px;
    height: 859px;
  }
  .card {
    position: absolute;
    top: 40px;
    width: 536px;
    height: 779px;
    background: var(--card);
    overflow: hidden;
  }
  .card--front { left: 40px; }
  .card--back { left: 623px; }

  .wordmark {
    position: absolute;
    left: 0;
    right: 0;
    top: 118px;
    margin: 0;
    text-align: center;
    color: var(--ink-light);
    font-family: "Nunito Sans", sans-serif;
    font-weight: 400;
  }
  .wordmark__name {
    display: block;
    font-size: 72px;
    line-height: 1.1;
    letter-spacing: 1px;
  }
  .wordmark__tagline {
    display: block;
    margin-top: 40px;
    font-size: 27px;
    letter-spacing: 2px;
  }

  .contact {
    position: absolute;
    left: 0;
    right: 0;
    top: 557px;
    text-align: center;
    color: var(--ink-light);
    font-family: "Nunito Sans", sans-serif;
    font-style: normal;
    font-weight: 400;
    font-size: 31px;
    line-height: 36px;
  }
  .contact__phone { margin-top: 12px; }

  .stamp-grid {
    position: absolute;
    left: 0;
    top: 0;
  }
  .stamp-slot { fill: var(--slot); }
  .stamp-slot--used { fill: var(--stamp); }

  .entry-field {
    position: absolute;
    top: 51px;
    width: 77px;
    height: 691px;
    background: var(--slot);
    border-radius: 8px;
  }
  .entry-field--name { left: 318px; }
  .entry-field--phone { left: 422px; }
  .entry-field__label {
    position: absolute;
    left: 50%;
    bottom: 18px;
    transform-origin: left bottom;
    transform: translateX(14px) rotate(-90deg);
    font-family: "Courier Prime", monospace;
    font-size: 40px;
    letter-spacing: 8px;
    line-height: 1;
    color: var(--label);
    white-space: nowrap;
  }
</style>
</head>
<body>
<div class="canvas">

  <section class="card card--front">
    <h1 class="wordmark">
      <span class="wordmark__name">The Lantern</span>
      <span class="wordmark__tagline">Coffee Bar &amp; Grill</span>
    </h1>
    <address class="contact">
      <div>14b Wattlebrook St</div>
      <div>Kelmarra NSW 2318</div>
      <div class="contact__phone">02 4817 6293</div>
    </address>
  </section>

  <section class="card card--back">
    <svg class="stamp-grid" width="300" height="779" viewBox="0 0 300 779">
      <circle class="stamp-slot stamp-slot--used" cx="98" cy="99" r="48" role="img" aria-label="Loyalty stamp"/>
      <circle class="stamp-slot stamp-slot--used" cx="220" cy="99" r="48" role="img" aria-label="Loyalty stamp"/>
      <circle class="stamp-slot stamp-slot--used" cx="98" cy="198" r="48" role="img" aria-label="Loyalty stamp"/>
      <circle class="stamp-slot stamp-slot--used" cx="220" cy="198" r="48" role="img" aria-label="Loyalty stamp"/>
      <circle class="stamp-slot stamp-slot--used" cx="98" cy="297" r="48" role="img" aria-label="Loyalty stamp"/>
      <circle class="stamp-slot" cx="220" cy="297" r="48"/>
      <circle class="stamp-slot" cx="98" cy="397" r="48"/>
      <circle class="stamp-slot" cx="220" cy="397" r="48"/>
      <circle class="stamp-slot" cx="98" cy="496" r="48"/>
      <circle class="stamp-slot" cx="220" cy="496" r="48"/>
      <circle class="stamp-slot" cx="98" cy="595" r="48"/>
      <circle class="stamp-slot" cx="220" cy="595" r="48"/>
      <circle class="stamp-slot" cx="98" cy="694" r="48"/>
      <circle class="stamp-slot" cx="220" cy="694" r="48"/>
    </svg>

    <div class="entry-field entry-field--name">
      <span class="entry-field__label">Name</span>
    </div>
    <div class="entry-field entry-field--phone">
      <span class="entry-field__label">Phone</span>
    </div>
  </section>

</div>
</body>
</html>
```